Kallomer Foundation
Project: Kallomer Foundation
Kallomer Foundation - Fund Raising
Creative Brief
Fund Raising
http://kallomer.org
Donation site, we should have area for current donation projection, companies that our offer vouchers to promote donation projects, creative image that translate the # of $$ donated to a specific project.
left side

```html
<!DOCTYPE html>
<html lang="en">
<head>
<meta charset="utf-8">
<title>Kallomer Foundation</title>
<link href="https://fonts.googleapis.com/css2?family=Open+Sans:ital,wght@0,400;0,600;0,700;1,400;1,700&display=swap" rel="stylesheet">
<style>
:root{
  --green-dark:#2f6e2f;
  --green-nav:#3b7d36;
  --green-btn:#2f7a2f;
  --green-init:#6db56f;
  --green-pale:#e5efcf;
  --pink:#f2c7c9;
  --blue-pale:#d8e7f1;
  --tan:#ecd4bd;
  --loan-bg:#fbeff6;
  --yellow:#fafbcc;
  --story-bg:#e4eaf3;
  --find-bg:#f5f5f5;
  --footer:#3f8d3f;
  --text:#333;
  --white:#fff;
  --btn-green:#6fb840;
}
*{box-sizing:border-box;margin:0;padding:0}
html,body{width:1200px;height:4161px;overflow:hidden}
body{font-family:"Open Sans",Arial,sans-serif;color:var(--text);position:relative;background:#fff}
section,header,footer{position:absolute;left:0;width:1200px}
.abs{position:absolute}
.ph{position:absolute}
.btn{display:inline-block;font-size:12px;padding:5px 14px;text-transform:uppercase;letter-spacing:.3px}
.btn-white{background:#fff;color:#333;border:1px solid #ccc}
.btn-green{background:var(--green-btn);color:#fff}
.frame{border:4px solid rgba(255,255,255,.7);box-shadow:0 0 0 1px rgba(0,0,0,.12)}
h2{font-weight:400;font-size:29px;line-height:1.1}
p{font-size:12.5px;line-height:21px}

/* header */
.site-header{top:0;height:73px}
.logo{left:140px;top:-4px;width:230px;height:72px;background:var(--green-nav);color:#fff;z-index:2;padding:0 8px}
.logo .name{font-size:42px;font-weight:700;line-height:48px;display:block}
.logo .sub{font-size:21px;line-height:20px;display:block;text-align:right;padding-right:10px}
.connect{right:155px;top:9px;font-size:13px;font-style:italic;font-weight:700;color:#444;display:flex;align-items:center;gap:6px}
.connect i{width:21px;height:21px;border-radius:50%;background:#333;display:inline-block}
.login{left:952px;top:5px;width:96px;height:26px;background:#8c2a1c;color:#fff;font-size:13px;font-weight:700;text-align:center;line-height:26px}
.nav{top:39px;height:34px;background:var(--green-nav)}
.nav ul{list-style:none;position:absolute;left:462px;top:0;display:flex}
.nav li{color:#fff;font-size:13px;font-weight:700;line-height:34px;padding:0 25px}
.nav li.active{background:#8c2a1c}

/* hero */
.hero{top:73px;height:468px;background:linear-gradient(90deg,#e8e6e0 0%,#c9c4b8 40%,#a79f90 60%,#d9c6a6 100%)}
.hero-box{left:140px;top:142px;width:393px;height:307px;background:rgba(30,30,30,.88);color:#fff;text-align:center;padding:18px 8px}
.hero-box h1{font-weight:400;font-size:31px}
.hero-box h3{font-style:italic;font-weight:400;font-size:21px;line-height:27px;margin-top:10px}
.hero-box p{font-size:12.5px;line-height:21px;margin-top:14px;padding:0 12px}
.hero-box .btn{margin-top:12px;text-transform:none;font-size:13.5px;padding:5px 22px}
.dots{left:985px;top:447px;display:flex;gap:6px}
.dots i{width:11px;height:11px;border-radius:50%;background:#ccc}
.dots i:first-child{background:#3b7d36}

/* about */
.about{top:541px;height:215px;background:linear-gradient(180deg,#8da6bb 0%,#b9c9d5 60%,#d3dde4 100%);text-align:center;color:#fff}
.about h2{margin-top:22px}
.about p{width:900px;margin:14px auto 0;color:#fff}
.about .btn{margin-top:14px}

/* feature rows */
.feature .text{top:0}
.feature h2{border-bottom:1px solid rgba(0,0,0,.15);padding-bottom:6px}
.initiatives{top:756px;height:281px;background:var(--green-init);color:#fff}
.initiatives h2{border-color:rgba(255,255,255,.6)}
.scholarship{top:1037px;height:283px;background:var(--green-pale)}
.fundraising{top:1320px;height:280px;background:var(--pink)}
.voucher{top:1600px;height:282px;background:var(--blue-pale)}

/* programs */
.programs{top:1882px;height:327px;background:var(--tan);text-align:center}
.programs h2,.completed h2{margin-top:14px}
.programs>p,.completed>p{width:840px;margin:8px auto 0;font-size:12px}
.map{width:278px;height:120px;top:127px;border:4px solid #fff;background:linear-gradient(135deg,#e8df9a,#cfe3a5 50%,#e3d89a)}
.pin{width:16px;height:16px;border-radius:50% 50% 50% 0;background:#c8202a;transform:rotate(-45deg)}
.map-cap{top:258px;width:278px;text-align:left;font-size:13px;line-height:19px;padding-left:26px}
.map-cap svg{position:absolute;left:4px;top:1px}

/* loans */
.loans{top:2209px;height:718px;background:var(--loan-bg)}
.loan-bar{left:140px;top:29px;width:918px;height:36px;background:var(--green-dark);color:#fff;font-size:21px;line-height:36px;padding-left:14px}
.loan-bar .sector{position:absolute;right:14px;top:8px;width:200px;height:21px;background:#fff;color:#999;font-size:12px;line-height:21px;padding-left:6px}
.loan-bar .sector:after{content:"";position:absolute;right:4px;top:4px;width:13px;height:13px;background:#555}
.loan-photo{left:150px;width:267px;height:162px;border:4px solid #fff;box-shadow:0 0 0 1px #ddd}
.loan-info{left:441px;width:307px;height:162px;background:#ddd;border-radius:3px;padding:10px 14px;font-size:11px;line-height:19px;letter-spacing:.5px}
.loan-info:before{content:"";position:absolute;left:-12px;top:30px;border:6px solid transparent;border-right-color:#ddd}
.loan-info h4{font-weight:400;font-size:15.5px;line-height:20px}
.loan-info b{display:block;font-size:11px}
.loan-info .btn{padding:0 6px;font-size:10.5px;background:#8c2a1c;color:#fff;line-height:15px;margin-top:2px}
.loan-give{left:780px;width:271px}
.bar{height:13px;border-radius:7px;background:#bbb;overflow:hidden}
.bar i{display:block;height:100%;width:78%;background:repeating-linear-gradient(135deg,#7fc24a 0 8px,#62a935 8px 16px)}
.stats{display:flex;justify-content:space-between;font-size:12px;line-height:14px;margin-top:11px;color:#555}
.amount{margin-top:8px;height:38px;border:1px solid #ddd;background:#fff;color:#aaa;font-style:italic;font-size:14px;text-align:center;line-height:36px}
.give-btn{margin-top:5px;height:51px;background:linear-gradient(#7cc44a,#5aa22c);color:#fff;font-size:24px;font-weight:600;text-align:center;line-height:51px;border-radius:2px}

/* completed */
.completed{top:2927px;height:319px;background:var(--yellow);text-align:center}
.done-photo{top:120px;width:215px;height:146px;border:3px solid #fff;box-shadow:0 0 0 1px #ccc}
.done-cap{top:277px;width:215px;font-size:14px;font-weight:700;color:#333}

/* stories */
.stories{top:3246px;height:340px;background:linear-gradient(90deg,#e5ebf2,#eef0f6 50%,#dfe6f1);text-align:center}
.story{top:0;width:420px}
.story h2{font-size:23px;margin-top:14px}
.avatar{width:140px;height:140px;border-radius:50%;border:4px solid #fff;margin:6px auto 0;box-shadow:0 0 0 1px #ccc}
.story p{font-size:12px;line-height:18px;margin-top:14px}
.story .btn{margin-top:8px}

/* find */
.find{top:3586px;height:247px;background:var(--find-bg);text-align:center}
.find h2{margin-top:28px;font-size:29px}
.find p{width:860px;margin:18px auto 0;font-size:12.5px}
.get-started{left:484px;top:184px;width:232px;height:46px;background:linear-gradient(#6cc148,#3c8e28);border-radius:3px;color:#fff;font-size:22px;font-weight:700;font-style:italic;line-height:46px;padding-left:18px;text-align:left}
.get-started span{position:absolute;right:0;top:0;width:50px;height:46px;background:#2f7a22;display:flex;align-items:center;justify-content:center}

/* partners */
.partners{top:3833px;height:140px;background:#fff}
.partners .label{left:147px;top:38px;font-size:21px;line-height:24px;color:#444}
.badge{top:36px;height:64px;background:#f2f2f2;border-radius:3px;display:flex;align-items:center;justify-content:center}
.badge i{display:block;background:#c8c8c8}

/* signup + footer */
.signup{top:3973px;height:49px;background:var(--green-dark);color:#fff}
.signup .title{left:144px;top:12px;font-size:19px}
.signup .note{left:295px;top:10px;font-size:11.5px;line-height:14px;width:290px}
.field{top:12px;height:27px;background:#fff;color:#aaa;font-style:italic;font-size:11px;line-height:27px;padding-left:8px}
.submit{left:982px;top:12px;width:76px;height:27px;background:#e8551c;color:#fff;font-weight:700;font-size:12px;text-align:center;line-height:27px}
.site-footer{top:4022px;height:139px;background:var(--footer);color:#fff;text-align:center}
.foot-nav{margin-top:28px;font-size:13px}
.foot-nav span{margin:0 28px}
.foot-social{margin-top:22px;display:flex;justify-content:center;gap:14px}
.foot-social i{width:18px;height:18px;border-radius:50%;background:#fff;display:block}
.copy{margin-top:22px;font-size:11.5px}
</style>
</head>
<body>

<header class="site-header">
  <div class="abs logo"><span class="name">Kallomer</span><span class="sub">Foundation</span></div>
  <div class="abs connect">Stay Connected : <i></i><i></i><i></i></div>
  <div class="abs login">LOGIN</div>
  <nav class="abs nav" style="width:1200px;left:0">
    <ul><li class="active">Home</li><li>About Us</li><li>Initiatives</li><li>Scholarships &amp; Awards</li><li>Fundraising</li></ul>
  </nav>
</header>

<section class="hero" role="img" aria-label="Photo of a smiling woman standing with four young children">
  <div class="abs hero-box">
    <h1>We can see you suffering</h1>
    <h3>Too many seniors live below the poverty line</h3>
    <p>These days it's not hard to look around and see so many people in need of help. There are people in need of financial assistance, seniors who are struggling during their golden years and communities that face on-going and new challenges every day.</p>
    <span class="btn btn-white">Learn more about our Care Aid Program</span>
  </div>
  <div class="abs dots"><i></i><i></i><i></i><i></i></div>
</section>

<section class="about">
  <h2>About Us</h2>
  <p>The Kallomer Foundation was created to honour Dr. Harlan P. Kallomer. Harlan was a remarkable individual who excelled at everything he chose to take on. He was a high academic achiever, was community oriented and liked recreational sports as well as competitive sports. Within four years after earning his PhD and starting his career Harlan obtained the status of a tenured professor.</p>
  <span class="btn btn-white">Read More</span>
</section>

<section class="feature initiatives">
  <div class="abs" style="left:140px;top:22px;width:475px">
    <h2>Initiatives</h2>
    <p style="margin-top:10px;font-size:12px">Our initiatives include Drinking Responsibly, Senior Programs, Youth Programs, Community Building, and Pet Tales.</p>
    <p style="margin-top:12px;font-size:12px">Lorem ipsum dolor sit amet, consectetuer adipiscing elit, sed diam nonummy nibh euismod tincidunt ut laoreet dolore magna aliquam erat volutpat.</p>
    <span class="btn btn-white" style="margin-top:24px">Read More</span>
  </div>
  <div class="ph frame" style="left:728px;top:29px;width:328px;height:232px;background:linear-gradient(135deg,#c9b9a3,#8f6f58 50%,#5a7a9c)" role="img" aria-label="Photo of a smiling multigenerational family on a sofa"></div>
</section>

<section class="feature scholarship">
  <div class="ph frame" style="left:142px;top:28px;width:328px;height:232px;background:linear-gradient(90deg,#2a4f93,#1d3a78)" role="img" aria-label="Poster of a football player: your support helps win games"></div>
  <div class="abs" style="left:520px;top:22px;width:520px">
    <h2 style="border:none">Scholarship &amp;<br>Awards</h2>
    <p style="margin-top:16px;font-size:12px">The Dr. Harlan P. Kallomer [Kal-oh-mer] Annual Community Service Entrance Award was established to foster and promote the prevention of drinking and driving. It pays tribute to Dr. Harlan P. Kallomer, an outstanding faculty member at Westbrook University.</p>
    <span class="btn btn-green" style="margin-top:16px">Read More</span>
  </div>
</section>

<section class="feature fundraising">
  <div class="abs" style="left:145px;top:18px;width:530px">
    <h2 style="border:none">Fundraising</h2>
    <p style="margin-top:12px;font-size:12px">When we think of fundraising we usually think of the traditional bake sales, going door to door selling chocolates, bottle drives and car washes to name just a few. Brindle Market was created to not only compliment the traditional fundraisers but to enhance local merchant's businesses.</p>
    <span class="btn btn-green" style="margin-top:14px">Read More</span>
  </div>
  <div class="ph frame" style="left:728px;top:28px;width:328px;height:232px;background:linear-gradient(135deg,#b89a78,#8a6a4e 50%,#c55a3a)" role="img" aria-label="Photo of a volunteer handing a basket of food to a senior"></div>
</section>

<section class="feature voucher">
  <div class="ph frame" style="left:142px;top:28px;width:328px;height:232px;background:linear-gradient(135deg,#9a7a64,#5f4a3e 50%,#b33c32)" role="img" aria-label="Photo of a family gathered around a computer"></div>
  <div class="abs" style="left:520px;top:20px;width:530px">
    <h2 style="border:none">Purchase a Voucher to<br>Support a Program</h2>
    <p style="margin-top:16px;font-size:12px">Lorem ipsum dolor sit amet, consectetuer adipiscing elit, sed diam nonummy nibh euismod tincidunt ut laoreet dolore magna aliquam erat volutpat. Ut wisi enim ad minim veniam, quis nostrud exerci tation ullamcorper suscipit lobortis nisl ut aliquip ex ea</p>
    <span class="btn btn-green" style="margin-top:16px">Read More</span>
  </div>
</section>

<section class="programs">
  <h2>Active Programs</h2>
  <p>Lorem ipsum dolor sit amet, consectetuer adipiscing elit, sed diam nonummy nibh euismod tincidunt ut laoreet dolore magna aliquam erat volutpat. Ut wisi enim ad minim veniam, quis nostrud exerci tation ullamcorper suscipit lobortis nisl ut aliquip ex ea</p>
  <div class="ph map" style="left:160px" role="img" aria-label="Street map of program location"><i class="abs pin" style="left:222px;top:66px"></i></div>
  <div class="ph map" style="left:462px" role="img" aria-label="Street map of program location"><i class="abs pin" style="left:140px;top:36px"></i></div>
  <div class="ph map" style="left:762px" role="img" aria-label="Street map of program location"><i class="abs pin" style="left:222px;top:66px"></i></div>
  <div class="abs map-cap" style="left:160px"><svg width="14" height="18" viewBox="0 0 14 18"><path d="M7 0a7 7 0 0 0-7 7c0 5 7 11 7 11s7-6 7-11a7 7 0 0 0-7-7z" fill="#333"/><circle cx="7" cy="7" r="2.5" fill="#ecd4bd"/></svg><b>132 Lorem ipsum</b> dolor sit amet conse ctetuer adipiscing eli</div>
  <div class="abs map-cap" style="left:462px"><svg width="14" height="18" viewBox="0 0 14 18"><path d="M7 0a7 7 0 0 0-7 7c0 5 7 11 7 11s7-6 7-11a7 7 0 0 0-7-7z" fill="#333"/><circle cx="7" cy="7" r="2.5" fill="#ecd4bd"/></svg><b>132 Lorem ipsum</b> dolor sit amet conse ctetuer adipiscing eli</div>
  <div class="abs map-cap" style="left:762px"><svg width="14" height="18" viewBox="0 0 14 18"><path d="M7 0a7 7 0 0 0-7 7c0 5 7 11 7 11s7-6 7-11a7 7 0 0 0-7-7z" fill="#333"/><circle cx="7" cy="7" r="2.5" fill="#ecd4bd"/></svg><b>132 Lorem ipsum</b> dolor sit amet conse ctetuer adipiscing eli</div>
</section>

<section class="loans">
  <div class="abs loan-bar">Fund A Loan<span class="sector">Sector</span></div>

  <div class="ph loan-photo" style="top:92px;background:linear-gradient(135deg,#c9b79c,#7c5c42)" role="img" aria-label="Photo of a baker at work"></div>
  <div class="abs loan-info" style="top:92px"><h4>SAMIR HADDAN</h4><b>Bakery, Egypt</b>Durch perfekte Kombination einzelner Online -Maßna hmen. Mitder richtigen Auswahl der Online-Marketing Tools lassen sich Kunden undLeads effizient und nbar quirieren.<br><span class="btn">Read More</span></div>
  <div class="abs loan-give" style="top:94px"><div class="bar"><i></i></div><div class="stats"><span>82%<br>Funded</span><span>$3256<br>Gifted</span><span>$4500<br>Goal</span></div><div class="amount">Enter your gift amount</div><div class="give-btn">ADD GIFT</div></div>

  <div class="ph loan-photo" style="top:310px;background:linear-gradient(135deg,#a8503a,#6e5a8c 50%,#c9a46e)" role="img" aria-label="Photo of a couple in a bookshop"></div>
  <div class="abs loan-info" style="top:310px"><h4>TOBIN MARSH</h4><b>Bakery, Egypt</b>Durch perfekte Kombination einzelner Online -Maßna hmen. Mitder richtigen Auswahl der Online-Marketing Tools lassen sich Kunden undLeads effizient und nbar quirieren.<br><span class="btn">Read More</span></div>
  <div class="abs loan-give" style="top:312px"><div class="bar"><i></i></div><div class="stats"><span>82%<br>Funded</span><span>$3256<br>Gifted</span><span>$4500<br>Goal</span></div><div class="amount">Enter your gift amount</div><div class="give-btn">ADD GIFT</div></div>

  <div class="ph loan-photo" style="top:528px;background:linear-gradient(135deg,#efe6d8,#c9a98a)" role="img" aria-label="Photo of a woman working at a shop counter"></div>
  <div class="abs loan-info" style="top:528px"><h4>LENA VAROSA</h4><b>Bakery, Egypt</b>Durch perfekte Kombination einzelner Online -Maßna hmen. Mitder richtigen Auswahl der Online-Marketing Tools lassen sich Kunden undLeads effizient und nbar quirieren.<br><span class="btn">Read More</span></div>
  <div class="abs loan-give" style="top:530px"><div class="bar"><i></i></div><div class="stats"><span>82%<br>Funded</span><span>$3256<br>Gifted</span><span>$4500<br>Goal</span></div><div class="amount">Enter your gift amount</div><div class="give-btn">ADD GIFT</div></div>
</section>

<section class="completed">
  <h2>Recently Completed Fundraisers</h2>
  <p>Lorem ipsum dolor sit amet, consectetuer adipiscing elit, sed diam nonummy nibh euismod tincidunt ut laoreet dolore magna aliquam erat volutpat. Ut wisi enim ad minim veniam, quis nostrud exerci tation ullamcorper suscipit lobortis nisl ut aliquip ex ea</p>
  <div class="ph done-photo" style="left:144px;background:linear-gradient(135deg,#d9d4c8,#8a7563)" role="img" aria-label="Photo of two schoolchildren"></div>
  <div class="ph done-photo" style="left:376px;background:linear-gradient(180deg,#5a86c8,#c9b48a)" role="img" aria-label="Photo of children playing football outdoors"></div>
  <div class="ph done-photo" style="left:609px;background:linear-gradient(135deg,#d8c4a0,#a47a4e)" role="img" aria-label="Photo of volunteers packing donation boxes"></div>
  <div class="ph done-photo" style="left:841px;background:linear-gradient(135deg,#c9ccd2,#7a6e68)" role="img" aria-label="Photo of seniors playing a board game"></div>
  <div class="abs done-cap" style="left:144px">Consectetuer Adipiscing</div>
  <div class="abs done-cap" style="left:376px">Ullamorper Suscipit Lobrtis</div>
  <div class="abs done-cap" style="left:609px">Dolore Magna Aliquam</div>
  <div class="abs done-cap" style="left:841px">Sectetuer Adipiscing</div>
</section>

<section class="stories">
  <div class="abs story" style="left:140px">
    <h2>Maren's Story</h2>
    <div class="avatar" style="background:linear-gradient(135deg,#e8c9b0,#b8866a)" role="img" aria-label="Portrait photo of a smiling senior man"></div>
    <p>A Message About Dr. Kallomer (pronounced Kal-oh-mer)</p>
    <p style="margin-top:6px">I believe that everyone who enters our world leaves distinct footprints behind; leaving an impression that tells a story about who we were and what we did...</p>
    <span class="btn btn-green">Read More</span>
  </div>
  <div class="abs story" style="left:622px">
    <h2>Share Your Story</h2>
    <div class="avatar" style="background:linear-gradient(135deg,#dcd6cc,#8d7e70)" role="img" aria-label="Portrait photo of a young man"></div>
    <p style="padding:0 30px">"Over the years I have become convinced that we learn best – and change – from hearing stories that strike a cord within us "</p>
    <p style="margin-top:6px">Elias Brandt</p>
    <span class="btn btn-green" style="margin-top:14px">Read More</span>
  </div>
</section>

<section class="find">
  <h2>Find a program in my community</h2>
  <p>Lorem ipsum dolor sit amet, consectetuer adipiscing elit, sed diam nonummy nibh euismod tincidunt ut laoreet dolore magna aliquam erat volutpat. Ut wisi enim ad minim veniam, quis nostrud exerci tation ullamcorper suscipit lobortis nisl ut aliquip ex eaLorem dolor sit amet, consectetuer adipiscing elit, sed diam nonummy nibh euismod tincidunt ut laoreet dolore magna</p>
  <div class="abs get-started">GET STARTED<span><svg width="16" height="18" viewBox="0 0 16 18"><path d="M3 2l9 7-9 7" fill="none" stroke="#fff" stroke-width="4"/></svg></span></div>
</section>

<section class="partners">
  <div class="abs label">We are<br>partnered with</div>
  <div class="abs badge" style="left:364px;width:134px"><i style="width:90px;height:26px;border-radius:13px"></i></div>
  <div class="abs badge" style="left:520px;width:186px"><i style="width:130px;height:30px"></i></div>
  <div class="abs badge" style="left:727px;width:134px"><i style="width:96px;height:34px"></i></div>
  <div class="abs badge" style="left:874px;width:118px"><i style="width:84px;height:40px;background:#d4222a"></i></div>
  <div class="abs badge" style="left:1002px;width:56px"><i style="width:34px;height:44px;background:#c9b97a"></i></div>
</section>

<section class="signup">
  <div class="abs title">Email Signup</div>
  <div class="abs note">Stay connected and receive email updates from Kallomer Foundation.</div>
  <div class="abs field" style="left:602px;width:134px">First Name</div>
  <div class="abs field" style="left:746px;width:226px">Email</div>
  <div class="abs submit">SUBMIT</div>
</section>

<footer class="site-footer">
  <div class="foot-nav"><span>Home</span>|<span>About Us</span>|<span>Initiatives</span>|<span>Scholarships &amp; Awards</span>|<span>Fundraising</span></div>
  <div class="foot-social"><i></i><i></i><i></i></div>
  <div class="copy">Kallomer Foundation © 2014 | All Rights Reserved</div>
</footer>

</body>
</html>
```